Photography Price List DL flyer

In need of a double sided DL flyer to list prices for a photography business that is in the real estate industry. Will need to include logo and be themed to match. Price details and contact information are in the pdf attached.

Below are links to the logo and photos that can be used on the flyer.

Logo
https://www.parcelnook.net/s/q7mwd2kfp0zltab/LogoFiles.zip?dl=0

Photos
https://www.parcelnook.net/s/h3vtr9gkw1jenoy/Website_Images.zip?dl=0
Updates

Sorry people the photo examples I put the wrong link. I have fixed it in the brief but the proper link is: https://www.parcelnook.net/s/h3vtr9gkw1jenoy/Website_Images.zip?dl=0

Also dimensions of a DL are 210mm x 99mm + 3m bleed. Thanks

Target Market(s)

Real estate agents

Industry/Entity Type

Business

Requirements
Must have
• Price lists and contact information

```html
<!DOCTYPE html>
<html lang="en">
<head>
<meta charset="utf-8">
<title>Clearview Photos – DL Price Flyer</title>
<link href="https://fonts.googleapis.com/css2?family=Josefin+Sans:wght@400;600&family=Lora:ital@1&display=swap" rel="stylesheet">
<style>
  :root{
    --bg:#e6e6e6;
    --paper:#ffffff;
    --charcoal:#434343;
    --leaf:#b5d56a;
    --coral:#d9606b;
    --text-light:#f2f2f2;
    --ink:#3d3d3d;
  }
  html,body{margin:0;padding:0;width:1200px;height:1000px;overflow:hidden;background:var(--bg);}
  body{position:relative;font-family:"Josefin Sans",sans-serif;}
  .flyer{position:absolute;background:var(--paper);}
  .flyer-front{left:145px;top:42px;width:910px;height:443px;}
  .flyer-back{left:145px;top:533px;width:912px;height:444px;}
  .panel{position:absolute;background:var(--charcoal);}
  .flyer-front .panel{left:27px;top:28px;width:855px;height:386px;}
  .flyer-back .panel{left:27px;top:28px;width:858px;height:387px;}
  .ribbon{position:absolute;background:var(--leaf);clip-path:polygon(0 0,100% 0,100% 100%,50% 78%,0 100%);}
  .ribbon-front{left:42px;top:0;width:151px;height:178px;text-align:center;}
  .ribbon-back{left:693px;top:0;width:107px;height:139px;text-align:center;}
  .ribbon-title{margin-top:68px;font-size:19px;letter-spacing:1px;color:var(--ink);line-height:1;}
  .ribbon-sub{font-family:"Lora",serif;font-style:italic;font-size:20px;color:var(--ink);letter-spacing:1px;margin-top:0;line-height:24px;}
  .ribbon-back .ribbon-sub{margin-top:56px;font-size:21px;}
  .brand-name{position:absolute;left:247px;top:80px;font-weight:600;font-size:32px;letter-spacing:3px;color:var(--coral);line-height:34px;text-align:center;}
  .brand-mark{position:absolute;left:500px;top:66px;width:84px;height:84px;border-radius:50%;background:var(--coral);}
  .contact{position:absolute;left:640px;top:65px;color:var(--text-light);font-size:14px;letter-spacing:0;}
  .contact-row{display:flex;align-items:center;gap:10px;height:29px;}
  .contact-row svg{width:16px;height:16px;fill:none;stroke:var(--coral);stroke-width:1.6;}
  .photo{position:absolute;}
  .pricing{position:absolute;left:652px;top:152px;color:var(--text-light);font-size:14px;letter-spacing:.4px;line-height:18.5px;}
  .price-head{color:var(--coral);font-size:14.5px;letter-spacing:1px;}
  .price-group{margin-bottom:14px;}
  .dot{color:var(--coral);}
  .back-mark{position:absolute;left:813px;top:340px;width:44px;height:44px;border-radius:50%;background:var(--coral);}
</style>
</head>
<body>

<section class="flyer flyer-front">
  <div class="panel"></div>
  <div class="ribbon ribbon-front">
    <div class="ribbon-title">REAL ESTATE</div>
    <div class="ribbon-sub">photography</div>
  </div>
  <div class="brand-name">CLEARVIEW<br>PHOTOS</div>
  <div class="brand-mark"></div>
  <div class="contact">
    <div class="contact-row"><svg viewBox="0 0 16 16"><path d="M3 1.5l3 3-1.5 2c1 2 2.5 3.5 4.5 4.5l2-1.5 3 3-2 2C6 14 2 10 1 3.5z"/></svg>0400 555 017</div>
    <div class="contact-row"><svg viewBox="0 0 16 16"><circle cx="8" cy="8" r="6.5"/><ellipse cx="8" cy="8" rx="3" ry="6.5"/><path d="M1.5 8h13"/></svg>clearviewphotos.com.au</div>
    <div class="contact-row"><svg viewBox="0 0 16 16"><rect x="1.5" y="3.5" width="13" height="9"/><path d="M1.5 3.5l6.5 5 6.5-5"/></svg>hello@clearviewphotos.com.au</div>
  </div>
  <div class="photo" role="img" aria-label="Balcony with pool overlooking bushland" style="left:42px;top:218px;width:338px;height:180px;background:linear-gradient(135deg,#5f7d3c,#a8b59a 55%,#5aa7c4);"></div>
  <div class="photo" role="img" aria-label="Open-plan dining area and kitchen" style="left:389px;top:218px;width:226px;height:180px;background:linear-gradient(160deg,#dfe3e3,#b8b2a4 60%,#8a7560);"></div>
  <div class="photo" role="img" aria-label="Bright bedroom with large windows" style="left:623px;top:218px;width:243px;height:180px;background:linear-gradient(160deg,#e8ecec,#c7c9c4 55%,#6d6a68);"></div>
</section>

<section class="flyer flyer-back">
  <div class="panel"></div>
  <div class="photo" role="img" aria-label="Brick house front with lawn and driveway" style="left:43px;top:44px;width:349px;height:170px;background:linear-gradient(180deg,#4f8fd6,#a7b3a6 45%,#5e9a3a);"></div>
  <div class="photo" role="img" aria-label="Queenslander home at twilight" style="left:400px;top:44px;width:108px;height:83px;background:linear-gradient(180deg,#5a6fa0,#9a6a4a);"></div>
  <div class="photo" role="img" aria-label="Living room with sofa" style="left:517px;top:44px;width:101px;height:83px;background:linear-gradient(180deg,#e4e4e0,#8a7f74);"></div>
  <div class="photo" role="img" aria-label="House exterior with garden" style="left:400px;top:136px;width:108px;height:78px;background:linear-gradient(180deg,#5b96d8,#d8d6cc 55%,#5f9440);"></div>
  <div class="photo" role="img" aria-label="Lounge room with timber floors" style="left:517px;top:136px;width:101px;height:78px;background:linear-gradient(160deg,#e6dcc8,#a9773f);"></div>
  <div class="photo" role="img" aria-label="Dining area with staircase" style="left:43px;top:223px;width:230px;height:178px;background:linear-gradient(160deg,#efeae0,#b27b3f 70%,#7a4a22);"></div>
  <div class="photo" role="img" aria-label="Backyard pool at dusk" style="left:282px;top:223px;width:110px;height:83px;background:linear-gradient(180deg,#4d6aa2,#c4906a 60%,#4aa2c0);"></div>
  <div class="photo" role="img" aria-label="Verandah with view" style="left:282px;top:315px;width:110px;height:86px;background:linear-gradient(180deg,#a8c7e6,#e4e4e0 55%,#8b6a4a);"></div>
  <div class="photo" role="img" aria-label="Living room with sofas and rug" style="left:401px;top:223px;width:217px;height:178px;background:linear-gradient(170deg,#f2f0ea,#c8b39a 60%,#8a5a32);"></div>
  <div class="ribbon ribbon-back">
    <div class="ribbon-sub">pricing</div>
  </div>
  <div class="pricing">
    <div class="price-group">
      <div class="price-head">PHOTOGRAPHY</div>
      <div>10 images <span class="dot">•</span> $149</div>
      <div>12 - 15 images <span class="dot">•</span> $179</div>
      <div>20+ images <span class="dot">•</span> $229</div>
    </div>
    <div class="price-group">
      <div class="price-head">TWILIGHT</div>
      <div>Add $100 to image package</div>
    </div>
    <div class="price-group">
      <div><span class="price-head">FLOORPLANS</span> $49</div>
    </div>
    <div class="price-group">
      <div class="price-head">VIDEO</div>
      <div>30 seconds <span class="dot">•</span> $150</div>
      <div>60 seconds <span class="dot">•</span> $200</div>
      <div>2 minutes <span class="dot">•</span> $300</div>
    </div>
  </div>
  <div class="back-mark"></div>
</section>

</body>
</html>
```